Coral Bay Dental Surgery Business Cards

Hi there

Can i please have a simple business card designed (front and back with a black background) using out white reverse logo and the same font used for the logo?
On the back we can just have the logo. Full details at the front part.
Here are the details:

Name of the surgery: Coral Bay | Dental Surgery
Name on the business card: Dr Owen Thackery
Credentials:
BDSc (KTL)
MSc Oral Implantology (Halvorsen, Frankfurt)
Fellow & Diplomate (Meridian Council of Restorative Prosthetics)

Email: owen.thackery@coralbaysmile.example
Address: 17 Lisgrove Rd Karrinyup
Website: coralbaysmile.example
Phone: 1800 316 482

We have attached our high res logo and a rudimentary version of the business card which is not necessarily what we want but gives all the details
We would like to have the print ready version. Thanks.

Contact Information for Business Card

website. credentials. qr code. address. phone number

Requirements
Must have
• QR code

```html
<!DOCTYPE html>
<html lang="en">
<head>
<meta charset="utf-8">
<title>Coral Bay Dental Surgery – Business Cards</title>
<link rel="stylesheet" href="https://fonts.googleapis.com/css2?family=Montserrat:wght@400;500;700&display=swap">
<style>
  :root {
    --backdrop: #d4d4d4;
    --card: #0b0b0b;
    --ink: #f2f2f2;
    --ink-soft: #dcdcdc;
    --pill: #efefef;
    --pill-icon: #111111;
    --qr-field: #e6e6e6;
  }
  * { box-sizing: border-box; margin: 0; padding: 0; }
  html, body {
    width: 1200px; height: 801px; overflow: hidden;
    background: var(--backdrop);
    font-family: "Montserrat", sans-serif;
    color: var(--ink);
  }
  .sheet {
    position: relative; width: 1200px; height: 801px;
    display: flex; align-items: center; justify-content: center; gap: 44px;
  }
  .card {
    position: relative; width: 520px; height: 300px;
    background: var(--card); border-radius: 18px;
    box-shadow: 0 14px 30px rgba(0,0,0,.22);
    overflow: hidden;
  }

  /* ---------- front ---------- */
  .brand-mark {
    position: absolute; left: 34px; top: 26px;
    display: flex; align-items: center; gap: 10px;
  }
  .brand-mark .dot { width: 14px; height: 14px; border-radius: 50%; background: var(--ink); flex: none; }
  .brand-mark .name {
    font-weight: 500; font-size: 14px; line-height: 1.25; letter-spacing: .08em;
    text-transform: uppercase; color: var(--ink);
  }
  .practitioner {
    position: absolute; right: 34px; top: 68px; text-align: right;
  }
  .practitioner .doctor { font-weight: 700; font-size: 25px; letter-spacing: .01em; line-height: 1; }
  .practitioner .practice { font-weight: 400; font-size: 9.5px; line-height: 1; margin-top: 7px; color: var(--ink-soft); }
  .divider-main {
    position: absolute; left: 34px; right: 34px; top: 122px;
    height: 1.5px; background: var(--ink);
  }

  .contact-rail {
    position: absolute; left: 34px; top: 138px;
    width: 28px; height: 124px; border-radius: 14px; background: var(--pill);
    display: flex; flex-direction: column; align-items: center; justify-content: space-around;
    padding: 8px 0;
  }
  .contact-rail svg { width: 12px; height: 12px; fill: var(--pill-icon); }
  .contact-list {
    position: absolute; left: 74px; top: 143px; list-style: none;
    font-size: 11px; font-weight: 400; line-height: 28px; color: var(--ink-soft);
  }
  .credentials {
    position: absolute; right: 34px; top: 138px; text-align: right;
    font-size: 10.5px; line-height: 17px; color: var(--ink-soft);
  }
  .qr-code {
    position: absolute; right: 34px; bottom: 24px;
    width: 54px; height: 54px; border-radius: 4px;
    background: var(--qr-field);
  }

  /* ---------- back ---------- */
  .card--back { display: flex; align-items: center; justify-content: center; }
  .brand-mark--large { position: static; gap: 18px; }
  .brand-mark--large .dot { width: 30px; height: 30px; }
  .brand-mark--large .name { font-size: 30px; letter-spacing: .1em; line-height: 1.2; }
</style>
</head>
<body>
<main class="sheet">

  <section class="card card--front" aria-label="Business card front">
    <div class="brand-mark">
      <span class="dot"></span>
      <span class="name">Coral Bay<br>Dental Surgery</span>
    </div>

    <div class="practitioner">
      <p class="doctor">Dr Owen Thackery</p>
      <p class="practice">Coral Bay | Dental Surgery</p>
    </div>
    <div class="divider-main"></div>

    <div class="contact-rail" aria-hidden="true">
      <svg viewBox="0 0 24 24"><path d="M12 2a7 7 0 0 0-7 7c0 5.2 7 13 7 13s7-7.8 7-13a7 7 0 0 0-7-7zm0 9.5A2.5 2.5 0 1 1 12 6.5a2.5 2.5 0 0 1 0 5z"/></svg>
      <svg viewBox="0 0 24 24"><path d="M6.6 10.8a15.1 15.1 0 0 0 6.6 6.6l2.2-2.2c.3-.3.7-.4 1-.2 1.1.4 2.3.6 3.6.6.6 0 1 .4 1 1V20c0 .6-.4 1-1 1A17 17 0 0 1 3 4c0-.6.4-1 1-1h3.5c.6 0 1 .4 1 1 0 1.3.2 2.5.6 3.6.1.3 0 .7-.2 1z"/></svg>
      <svg viewBox="0 0 24 24"><path d="M2 5h20v14H2zm2 2v.4l8 5.2 8-5.2V7zm0 2.8V17h16V9.8l-8 5.2z"/></svg>
      <svg viewBox="0 0 24 24"><path d="M5 2l14 10-6.2 1.3L16.5 21l-2.8 1.2-3.7-7.8L5 18.5z"/></svg>
    </div>
    <ul class="contact-list">
      <li>17 Lisgrove Rd Karrinyup</li>
      <li>1800 316 482</li>
      <li>owen.thackery@coralbaysmile.example</li>
      <li>www.coralbaysmile.example</li>
    </ul>

    <div class="credentials">
      <p>Credentials:</p>
      <p>BDSc (KTL)</p>
      <p>MSc Oral Implantology</p>
      <p>Fellow &amp; Diplomate</p>
    </div>
    <div class="qr-code" role="img" aria-label="QR code linking to www.coralbaysmile.example"></div>
  </section>

  <section class="card card--back" aria-label="Business card back">
    <div class="brand-mark brand-mark--large">
      <span class="dot"></span>
      <span class="name">Coral Bay<br>Dental Surgery</span>
    </div>
  </section>

</main>
</body>
</html>
```